Web Developer Needs a Business Card Design

I need a personal business card design that represents me as a web developer for potential employers. I would like the background to be a dark color on the front for contrast with my logo and name. The back will have all my information along with a smaller version of the logo. I want something with a modern look and feel, not too conservative. This will be used for potential employers and freelance work.

Industry/Entity Type

Business

Contact Information for Business Card

Front should have my logo and name. The back should have all my personal information which would include: name: Tom Brevardi, phone: 570-614-9083, email: tombrevardi@mailwisp.com, website url: www.tombrevardi.com, logo, web developer.

Font styles to use
Sans Serif

Requirements
Must have
• Must include my logo. The color palette base color will be the logo color.

```html
<!DOCTYPE html>
<html lang="en">
<head>
<meta charset="utf-8">
<title>Tom Brevardi — Business Card</title>
<link rel="stylesheet" href="https://fonts.googleapis.com/css2?family=Roboto:wght@400;500&display=swap">
<style>
  :root {
    --backdrop: #8a7358;
    --ink-black: #0b0b0b;
    --mint: #8fd6cc;
    --paper: #f3f3f3;
    --text-dark: #2a2a2a;
    --text-light: #ffffff;
  }
  * { margin: 0; padding: 0; box-sizing: border-box; }
  html, body {
    width: 1200px; height: 902px; overflow: hidden;
    background: var(--backdrop);
    font-family: "Roboto", Arial, sans-serif;
  }
  .stage { position: relative; width: 1200px; height: 902px; }
  .card {
    position: absolute; width: 520px; height: 297px;
    border-radius: 4px; overflow: hidden;
    box-shadow: 0 14px 30px rgba(0,0,0,.45);
  }
  .card-front { left: 70px; top: 80px; background: var(--ink-black); }
  .card-back { left: 610px; top: 525px; background: var(--paper); }

  .brand-mark {
    position: absolute; display: flex; align-items: center; gap: 12px;
    color: var(--mint); font-weight: 500;
  }
  .brand-mark .dot { background: var(--mint); border-radius: 50%; flex: none; }
  .card-front .brand-mark { left: 0; right: 0; top: 92px; justify-content: center; font-size: 34px; }
  .card-front .brand-mark .dot { width: 26px; height: 26px; }
  .front-name {
    position: absolute; right: 46px; bottom: 48px;
    color: var(--text-light); font-size: 36px; font-weight: 400;
    letter-spacing: 1px;
  }

  .back-art { position: absolute; inset: 0; }
  .card-back .brand-mark { left: 0; right: 0; top: 62px; justify-content: center; font-size: 26px; }
  .card-back .brand-mark .dot { width: 20px; height: 20px; }
  .identity { position: absolute; left: 34px; top: 222px; color: var(--text-dark); }
  .identity .person { font-size: 27px; font-weight: 400; }
  .identity .role { font-size: 14px; text-align: right; margin-top: 1px; }
  .divider { position: absolute; left: 262px; top: 200px; width: 1px; height: 80px; background: var(--text-dark); }
  .contacts { position: absolute; left: 282px; top: 203px; list-style: none; color: var(--text-dark); font-size: 14px; }
  .contacts li { display: flex; align-items: center; gap: 9px; height: 25px; }
  .contacts svg { width: 11px; height: 11px; flex: none; }
</style>
</head>
<body>
<main class="stage">
  <section class="card card-front">
    <div class="brand-mark"><span class="dot"></span><span>brevardi</span></div>
    <div class="front-name">TOM BREVARDI</div>
  </section>

  <section class="card card-back">
    <svg class="back-art" viewBox="0 0 520 297" aria-hidden="true">
      <polygon points="0,0 520,0 520,150 498,176 22,176 0,150" fill="var(--ink-black)"/>
      <polyline points="0,160 24,184 496,184 520,160" fill="none" stroke="var(--mint)" stroke-width="6"/>
    </svg>
    <div class="brand-mark"><span class="dot"></span><span>brevardi</span></div>
    <div class="identity">
      <div class="person">Tom Brevardi</div>
      <div class="role">web developer</div>
    </div>
    <div class="divider"></div>
    <ul class="contacts">
      <li><svg viewBox="0 0 12 12"><path d="M2 1h3l1 3-1.5 1a6 6 0 0 0 2.5 2.5L8 6l3 1v3a1 1 0 0 1-1 1A9 9 0 0 1 1 2a1 1 0 0 1 1-1z" fill="var(--text-dark)"/></svg>570-614-9083</li>
      <li><svg viewBox="0 0 12 12"><rect x="0.5" y="2" width="11" height="8" fill="var(--text-dark)"/><path d="M1 3l5 3.5L11 3" stroke="#fff" fill="none"/></svg>tombrevardi@mailwisp.com</li>
      <li><svg viewBox="0 0 12 12"><circle cx="6" cy="6" r="5" fill="none" stroke="var(--text-dark)" stroke-width="1.5"/><path d="M1 6h10M6 1c-2 3-2 7 0 10M6 1c2 3 2 7 0 10" stroke="var(--text-dark)" fill="none"/></svg>www.tombrevardi.com</li>
    </ul>
  </section>
</main>
</body>
</html>
```